Business Card Design Project

In addition to the logo design we want a professional and contemporary business card for a talent management agency. We provide management services to creative artists and want to communicate a professional creative vibe.
Updates

Reason: Sorry didnt realise I had put such a short timeline on it.

Target Market(s)

The business deals with creative artists and other industry professionals

Industry/Entity Type

Artists

Colors

Designer to choose colors to be used in the design.

Requirements
Must have
• Logo
Address
Phone
Email

```html
<!DOCTYPE html>
<html lang="en">
<head>
<meta charset="utf-8">
<title>Norvale Artists – Business Card</title>
<link href="https://fonts.googleapis.com/css2?family=Arimo:wght@400;700&display=swap" rel="stylesheet">
<style>
  :root {
    --stage: #3b3431;
    --card-black: #1d1d1f;
    --card-grey: #4b4b4d;
    --card-dark: #252527;
    --ink: #ffffff;
    --ink-soft: #d9d9d9;
    --accent-fade: #8a8a8a;
  }
  * { margin: 0; padding: 0; box-sizing: border-box; }
  html, body { width: 1200px; height: 741px; overflow: hidden; }
  body {
    background: var(--stage);
    font-family: "Arimo", Arial, sans-serif;
    color: var(--ink);
    position: relative;
  }
  .card {
    position: absolute;
    top: 216px;
    width: 540px;
    height: 309px;
    border-radius: 3px;
    overflow: hidden;
    box-shadow: 0 10px 30px rgba(0,0,0,.45);
  }
  .card-back { left: 40px; background: var(--card-black); }
  .card-front { left: 620px; background: var(--card-grey); }

  .brand {
    display: flex;
    align-items: center;
    gap: 8px;
    font-weight: 700;
    color: var(--ink);
    white-space: nowrap;
  }
  .brand-dot {
    border: 3px solid var(--ink);
    border-radius: 50%;
    flex: none;
  }

  .card-back .brand { position: absolute; right: 34px; bottom: 92px; font-size: 26px; }
  .card-back .brand-dot { width: 36px; height: 36px; }
  .card-back .web {
    position: absolute; right: 36px; bottom: 60px;
    font-size: 15px; letter-spacing: 4px; color: var(--ink-soft);
  }

  .front-shape { position: absolute; inset: 0; }
  .person { position: absolute; left: 0; top: 112px; display: flex; gap: 14px; }
  .person-bar {
    width: 22px; height: 40px;
    background: linear-gradient(90deg, var(--ink), var(--accent-fade));
  }
  .person-name { font-size: 22px; font-weight: 700; line-height: 1.1; }
  .person-role { font-size: 12px; color: var(--ink-soft); margin-top: 4px; }

  .card-front .brand { position: absolute; right: 26px; top: 52px; font-size: 20px; }
  .card-front .brand-dot { width: 30px; height: 30px; border-width: 2.5px; }

  .contacts {
    position: absolute; right: 22px; top: 148px;
    list-style: none; text-align: right;
  }
  .contacts li {
    display: flex; justify-content: flex-end; align-items: center;
    gap: 12px; font-size: 15px; height: 28px;
  }
  .contacts svg { width: 16px; height: 16px; fill: var(--ink); flex: none; }
</style>
</head>
<body>
  <section class="card card-back">
    <div class="brand"><span class="brand-dot"></span>Norvale Artists</div>
    <div class="web">www.website.com</div>
  </section>

  <section class="card card-front">
    <svg class="front-shape" viewBox="0 0 540 309" aria-hidden="true">
      <path d="M345 0 C300 70 370 120 310 185 C265 235 262 275 268 309 L540 309 L540 0 Z" fill="var(--card-dark)"/>
      <path d="M345 0 C300 70 370 120 310 185 C265 235 262 275 268 309" fill="none" stroke="var(--ink)" stroke-width="5"/>
    </svg>

    <div class="person">
      <span class="person-bar"></span>
      <div>
        <div class="person-name">Ellis Marrow</div>
        <div class="person-role">Developer</div>
      </div>
    </div>

    <div class="brand"><span class="brand-dot"></span>Norvale Artists</div>

    <ul class="contacts">
      <li>Type your location here
        <svg viewBox="0 0 16 16"><path d="M8 0a5.5 5.5 0 0 0-5.5 5.5C2.5 10 8 16 8 16s5.5-6 5.5-10.5A5.5 5.5 0 0 0 8 0zm0 7.5a2 2 0 1 1 0-4 2 2 0 0 1 0 4z"/></svg></li>
      <li>hello@norvale.com
        <svg viewBox="0 0 16 16"><path d="M0 3h16v1.5L8 9 0 4.5z M0 6l8 4.5L16 6v7H0z"/></svg></li>
      <li>(+84) 0123 456 789
        <svg viewBox="0 0 16 16"><path d="M3.5 0l3 3.5-1.8 2.2a9 9 0 0 0 5.6 5.6l2.2-1.8 3.5 3-2 3.5C7 15.5.5 9 0 2z"/></svg></li>
      <li>www.website.com
        <svg viewBox="0 0 16 16"><path d="M8 0a8 8 0 1 0 0 16A8 8 0 0 0 8 0zm0 1.5c.9 0 1.9 1.6 2.3 4H5.7C6.1 3.1 7.1 1.5 8 1.5zM1.7 7h3.8v2H1.7a6.5 6.5 0 0 1 0-2zm5.3 0h2v2H7zm3.5 0h3.8a6.5 6.5 0 0 1 0 2h-3.8zM5.7 10.5h4.6c-.4 2.4-1.4 4-2.3 4s-1.9-1.6-2.3-4z"/></svg></li>
    </ul>
  </section>
</body>
</html>
```